Business Card Design Project (Beer industry)

I am seeking a redesign of my business card. I am looking for something that will really stand out in both texture and feel. Something more on the modern side then traditional. Nothing die cut shaped like a beer mug please.

The card is used mostly for other industry professionals, as well as bar and restaurant owners. My title is Strategy & Acquisitions. If you would like to somehow incorporate that theme, that may work.

My business is craft and imported beer. Nothing fizzy and yellow, so my products are more on the upscale side.
Updates

I was able to update my logo in .ai and .tif format. I hope that helps. 

Thank you all for your creative ideas. I have uploaded my current business card in pdf format, as well as our logo in .eps file format. We are excited about the submissions so far and want to thank you all again.

PS Please do not include fax number in future submissions, as we are looking for something more creative and a fax says 1999 and not 2015, which is the message we are going for, without being futuristic. 

Thank you all once again for all of your submissions. If we would consider a two sided card, we would like the opposite side not to be the same as the front. The styles we have seen so far, it appears the front and back are too similar. Again, a two sided card is not required. Thank you and we look forward to pushing the boundaries of your creativity. Cheers

Target Market(s)

My card would mostly go to bar and restaurant operators as well as other beer industry professionals

Industry/Entity Type

Restaurant

Requirements
Nice to have
• Two sided would be considered, although not required
Should not have
• Anything die cut shaped like a beer mug.

```html
<!DOCTYPE html>
<html lang="en">
<head>
<meta charset="utf-8">
<title>Harbor Keg – Business Card</title>
<link rel="stylesheet" href="https://fonts.googleapis.com/css2?family=Questrial&family=Lora:ital,wght@1,500&display=swap">
<style>
  :root {
    --page-bg: #2a2623;
    --card-bg: #151515;
    --card-bg-light: #242424;
    --text-main: #d6d6d6;
    --text-soft: #a9a9a9;
    --rule: #5c5c5c;
    --stripe-blue: #1f4d8c;
    --stripe-gold: #e3b43a;
    --stripe-red: #7a1a12;
    --brand: #e3b43a;
  }
  * { margin: 0; padding: 0; box-sizing: border-box; }
  html, body { width: 1200px; height: 900px; overflow: hidden; }
  body {
    background: var(--page-bg);
    font-family: "Questrial", "Century Gothic", sans-serif;
    color: var(--text-main);
    position: relative;
  }
  .card {
    position: absolute;
    left: 180px; top: 210px;
    width: 840px; height: 480px;
    border-radius: 22px;
    background: radial-gradient(ellipse at 50% 35%, var(--card-bg-light), var(--card-bg) 70%);
    box-shadow: 0 18px 40px rgba(0,0,0,.55);
    overflow: hidden;
  }
  .stripes { position: absolute; left: 0; top: 0; width: 840px; height: 480px; }
  .tagline {
    position: absolute;
    right: 26px; top: 52px;
    font-family: "Lora", Georgia, serif;
    font-style: italic;
    font-weight: 500;
    font-size: 19px;
    color: #ececec;
    transform: rotate(-4deg);
    transform-origin: right bottom;
  }
  .brand {
    position: absolute;
    left: 40px; top: 172px;
    display: flex; align-items: center; gap: 10px;
    font-size: 28px;
    line-height: 1;
    color: var(--brand);
    letter-spacing: .5px;
  }
  .brand-mark { width: 14px; height: 14px; background: var(--brand); }
  .person { position: absolute; left: 330px; top: 182px; text-align: center; width: 220px; }
  .person-name { font-size: 26px; font-weight: 700; color: #e6e6e6; }
  .person-title { font-size: 13px; color: var(--text-soft); margin-top: 2px; }
  .contact-group {
    position: absolute;
    border-left: 1px solid var(--rule);
    padding-left: 26px;
    display: flex; flex-direction: column; gap: 14px;
  }
  .contact-group.online { left: 540px; top: 222px; }
  .contact-group.phones { left: 165px; top: 322px; }
  .contact-row { display: flex; align-items: center; gap: 16px; font-size: 19px; color: var(--text-main); letter-spacing: .4px; }
  .contact-row svg { width: 20px; height: 20px; flex: none; }
  .rule { position: absolute; height: 1px; background: var(--rule); }
  .rule.upper { left: 540px; right: 0; top: 300px; }
  .rule.lower { left: 0; right: 0; top: 448px; }
  .address {
    position: absolute; left: 0; right: 0; top: 414px;
    text-align: center; font-size: 19px; color: var(--text-main); letter-spacing: .4px;
  }
</style>
</head>
<body>
  <main class="card">
    <svg class="stripes" viewBox="0 0 840 480" aria-hidden="true">
      <polygon points="0,128 840,68 840,76 0,136" fill="var(--stripe-blue)"/>
      <polygon points="0,139 840,79 840,85 0,145" fill="var(--stripe-gold)"/>
      <polygon points="0,148 840,88 840,95 0,155" fill="var(--stripe-red)"/>
    </svg>
    <p class="tagline">Premier Craft &amp; Import Beer Distributor</p>

    <div class="brand"><span class="brand-mark"></span>Harbor Keg</div>

    <div class="person">
      <p class="person-name">Dan Kessler</p>
      <p class="person-title">sales manager</p>
    </div>

    <div class="contact-group online">
      <div class="contact-row">
        <svg viewBox="0 0 20 20" aria-hidden="true"><circle cx="10" cy="10" r="3.5" fill="none" stroke="#999" stroke-width="1.6"/><path d="M13.5 7v4.5a2 2 0 0 0 4 0V10a7.5 7.5 0 1 0-3 6" fill="none" stroke="#999" stroke-width="1.6"/></svg>
        dkessler@mailbox.com
      </div>
      <div class="contact-row">
        <svg viewBox="0 0 20 20" aria-hidden="true"><path d="M2 10 10 3l8 7h-2.5v7h-4v-4.5h-3V17h-4v-7z" fill="#999"/></svg>
        www.harborkegusa.com
      </div>
    </div>
    <div class="rule upper"></div>

    <div class="contact-group phones">
      <div class="contact-row">
        <svg viewBox="0 0 20 20" aria-hidden="true"><rect x="6" y="2" width="8" height="16" rx="1.5" fill="none" stroke="#999" stroke-width="1.6"/><line x1="9" y1="15.5" x2="11" y2="15.5" stroke="#999" stroke-width="1.4"/></svg>
        (917) 555-0148
      </div>
      <div class="contact-row">
        <svg viewBox="0 0 20 20" aria-hidden="true"><circle cx="10" cy="10" r="8" fill="none" stroke="#999" stroke-width="1.4"/><path d="M7 6.2c-.8.8-.7 2.8 1.3 4.9s4 2.2 4.8 1.4l-1.4-1.6-1.1.6c-.8-.4-1.7-1.3-2.1-2.1l.6-1.1z" fill="#999"/></svg>
        (718) 555-0192
      </div>
    </div>

    <p class="address">42 Foundry Street Brooklyn, NY 11201</p>
    <div class="rule lower"></div>
  </main>
</body>
</html>
```